Mobile Oil Change company needs a flyer to promote new business

We need a flyer to 1) print & handout and 2) email out to potential customers. We are a mobile oil change company that comes to our customer locations to perform the work instead of customers going to traditional oil change companies. We have a 21 point inspection with our oil change. (21 point inspection details will not be on the flyer). Would like to keep the flyer simple but creative. I'm attaching 1) the write-up we created, 2) our logo (logo color is dark teal on white but other combinations are included if you wanted to propose a different color combination), and 3) additional services we offer. Logo font is Alegreya Sans.
Would like the additional services listed with icons and brief descriptions (similar to attachment) without pricing. Company website for reference is www.brindlefleetcare.com.

Target Market(s)

Companies with many service vehicles such as Oil & Gas service companies, heating and air conditioning companies, utility companies, police departments, etc. Companies that prioritize convenience and maintenance first.

Font styles to use
Sans Serif

Colors
00a990

Requirements
Must have
• Simple but creative design with our logo at top of the flyer. Additional Services (details in document supplied) can be smaller and less prominent than other "main" content listed in the CONTENT document supplied.
Should not have
• Do not use animated character graphics in the flyer and limit (1) stock photos to A small area in the flyer.

```html
<!DOCTYPE html>
<html lang="en">
<head>
<meta charset="utf-8">
<title>Brindle Fleet Care – Mobile Oil Change Flyer</title>
<link rel="stylesheet" href="https://fonts.googleapis.com/css2?family=Roboto:wght@400;500;700&family=Roboto+Condensed:ital,wght@0,300;0,400;0,700;1,700&display=swap">
<style>
  :root {
    --teal: #00a990;
    --deep-teal: #154f52;
    --amber: #c98a2c;
    --ink: #3d4446;
    --navy-ink: #1f4a55;
    --white: #ffffff;
  }
  * { box-sizing: border-box; margin: 0; padding: 0; }
  html, body { width: 981px; height: 1200px; overflow: hidden; background: var(--white); }
  .flyer { position: relative; width: 981px; height: 1200px; background: var(--white); font-family: "Roboto", sans-serif; overflow: hidden; }

  .hero-photo { position: absolute; left: 560px; top: 172px; width: 421px; height: 420px;
    background: radial-gradient(ellipse at 40% 35%, #e9d9a6 0%, #ddd6c2 18%, #e6e6e6 45%, rgba(255,255,255,0) 80%); }

  .header-band { position: absolute; left: 0; top: 57px; width: 981px; height: 115px; background: var(--deep-teal); }
  .brand-box { position: absolute; left: 75px; top: 56px; width: 353px; height: 118px; background: var(--white);
    border-radius: 0 26px 26px 26px; display: flex; align-items: center; justify-content: center; gap: 12px; }
  .brand-mark { width: 18px; height: 18px; border-radius: 50%; background: var(--teal); }
  .brand-name { font-family: "Roboto Condensed", sans-serif; font-weight: 700; font-size: 40px; color: var(--teal); letter-spacing: 0.5px; }

  .tagline { position: absolute; left: 476px; top: 70px; font-family: "Roboto Condensed", sans-serif; }
  .tagline-main { font-size: 66px; font-weight: 700; color: var(--teal); line-height: 1; letter-spacing: 1px; }
  .tagline-sub { font-size: 28px; font-weight: 400; color: var(--amber); line-height: 1; margin-top: 4px; }

  .process-title { position: absolute; left: 75px; top: 226px; width: 840px; font-family: "Roboto Condensed", sans-serif;
    font-weight: 700; font-size: 27px; line-height: 31px; color: var(--teal); }
  .process-steps { position: absolute; left: 75px; top: 310px; list-style: none; font-size: 21px; color: var(--ink); }
  .process-steps li { height: 28.7px; line-height: 28.7px; }
  .step-num { display: inline-block; width: 36px; color: var(--teal); font-weight: 700; }

  .highlights { position: absolute; left: 77px; top: 480px; list-style: none; font-size: 20px; color: var(--navy-ink); }
  .highlights li { height: 24.5px; line-height: 24.5px; display: flex; align-items: center; gap: 10px; }
  .drop { width: 10px; height: 14px; flex: none; }

  .services-panel { position: absolute; left: 33px; top: 585px; width: 917px; height: 306px; background: var(--deep-teal);
    border-radius: 0 48px 0 48px; }
  .service { position: absolute; display: flex; gap: 16px; }
  .service-icon { width: 56px; height: 50px; flex: none; }
  .service-title { font-family: "Roboto Condensed", sans-serif; font-size: 17px; color: var(--teal); line-height: 20px; }
  .service-desc { font-size: 12px; color: var(--white); line-height: 15px; font-weight: 500; }

  .product-photo { position: absolute; left: 0; top: 905px; width: 487px; height: 295px;
    background: linear-gradient(120deg, #f0b33a 0%, #cfd3d6 30%, #b8bcc0 50%, #d7302a 75%, #ffffff 100%); opacity: 0.85; }

  .contact { position: absolute; left: 487px; top: 930px; width: 494px; text-align: center; font-family: "Roboto Condensed", sans-serif; }
  .contact-label { font-weight: 300; font-size: 35px; color: var(--navy-ink); display: flex; align-items: center; justify-content: center; gap: 8px; line-height: 44px; }
  .contact-label::before, .contact-label::after { content: ""; width: 36px; height: 2px; background: var(--navy-ink); }
  .contact-phone { font-weight: 700; font-size: 52px; color: var(--navy-ink); line-height: 58px; margin-bottom: 4px; }
  .contact-email { font-weight: 700; font-style: italic; font-size: 27px; color: var(--navy-ink); line-height: 36px; margin-bottom: 12px; }
  .contact-web { font-weight: 700; font-size: 32px; color: var(--teal); line-height: 40px; }
</style>
</head>
<body>
<main class="flyer">
  <div class="hero-photo" role="img" aria-label="Photo of golden motor oil pouring from a bottle, softly faded"></div>

  <header>
    <div class="header-band"></div>
    <div class="brand-box">
      <span class="brand-mark"></span>
      <span class="brand-name">Brindle Fleet Care</span>
    </div>
    <div class="tagline">
      <div class="tagline-main">HASSLE FREE</div>
      <div class="tagline-sub">OIL CHANGES ON YOUR TERMS</div>
    </div>
  </header>

  <h2 class="process-title">OUR SIMPLE 5-STEP PROCESS LETS YOU SCHEDULE AN APPOINTMENT &amp; GET SERVICE TO SAVE TIME &amp; MONEY:</h2>
  <ol class="process-steps">
    <li><span class="step-num">1)</span>Call or email us to schedule service</li>
    <li><span class="step-num">2)</span>Our highly trained technicians come to you for service</li>
    <li><span class="step-num">3)</span>Service is performed quickly on your vehicle</li>
    <li><span class="step-num">4)</span>Pay agreed-upon pricing and receipt is emailed to you</li>
    <li><span class="step-num">5)</span>Services performed are tracked electronically &amp; reminders created</li>
  </ol>

  <ul class="highlights">
    <li><svg class="drop" viewBox="0 0 10 14"><path d="M5 0 C5 4 0 7 0 10 A5 4 0 0 0 10 10 C10 7 5 4 5 0Z" fill="#00a990"/></svg>High quality synthetic oil used is best suited for commercial vehicles</li>
    <li><svg class="drop" viewBox="0 0 10 14"><path d="M5 0 C5 4 0 7 0 10 A5 4 0 0 0 10 10 C10 7 5 4 5 0Z" fill="#00a990"/></svg>Service includes a 21-point inspection</li>
    <li><svg class="drop" viewBox="0 0 10 14"><path d="M5 0 C5 4 0 7 0 10 A5 4 0 0 0 10 10 C10 7 5 4 5 0Z" fill="#00a990"/></svg>Additional services are available</li>
  </ul>

  <section class="services-panel" aria-label="Additional services">
    <div class="service" style="left:49px;top:48px">
      <svg class="service-icon" viewBox="0 0 56 50" fill="none" stroke="#c98a2c" stroke-width="2"><rect x="4" y="3" width="46" height="44"/><path d="M19 3v44M35 3v44M8 12h8M8 20h8M8 28h8M8 36h8M23 12h8M23 20h8M23 28h8M23 36h8M39 12h8M39 20h8M39 28h8M39 36h8"/></svg>
      <div><div class="service-title">ENGINE AIR FILTER REPLACEMENT</div><div class="service-desc">Maintain optimum engine performance.<br>Recommended every 15,000-30,000 miles.</div></div>
    </div>
    <div class="service" style="left:464px;top:52px">
      <svg class="service-icon" viewBox="0 0 56 50" fill="none" stroke="#c98a2c" stroke-width="2"><rect x="10" y="2" width="36" height="46" rx="4"/><path d="M2 18c8-6 16 6 24 0s16 6 28 0M2 28c8-6 16 6 24 0s16 6 28 0M2 38c8-6 16 6 24 0"/></svg>
      <div><div class="service-title">CABIN AIR FILTER REPLACEMENT</div><div class="service-desc">Maintain a clean A/C and fan system.<br>Recommended every 12 month or 15,000-25,000 miles.</div></div>
    </div>
    <div class="service" style="left:49px;top:130px">
      <svg class="service-icon" viewBox="0 0 56 50" fill="none" stroke="#c98a2c" stroke-width="2"><path d="M4 16l24-8 24 8-24 28z"/><path d="M28 10v14M20 40l14-30"/></svg>
      <div><div class="service-title">WIPERBLADE REPLACEMENT</div><div class="service-desc">Maintain Excellent visibility on the road.<br>Recommended every 6-12 month.</div></div>
    </div>
    <div class="service" style="left:464px;top:130px">
      <svg class="service-icon" viewBox="0 0 56 50" fill="none" stroke="#c98a2c" stroke-width="2"><circle cx="28" cy="25" r="21"/><circle cx="28" cy="25" r="15"/><circle cx="28" cy="27" r="4"/><path d="M14 22h10M32 22h10M28 31v9"/></svg>
      <div><div class="service-title">POWER STEERING FLUID FLUSH</div><div class="service-desc">Maintain proper power steering system health.<br>Recommended every 30,000-60,000 miles.</div></div>
    </div>
    <div class="service" style="left:49px;top:212px">
      <svg class="service-icon" viewBox="0 0 56 50" fill="none" stroke="#c98a2c" stroke-width="2"><rect x="6" y="4" width="26" height="42" rx="3"/><rect x="11" y="9" width="16" height="10"/><path d="M32 14l8 6v16a4 4 0 0 0 8 0V22l-6-8M2 46h36"/></svg>
      <div><div class="service-title">FUEL SYSTEM TREATMENT</div><div class="service-desc">Clean your fuel system and injectors to<br>improve fuel economy.</div></div>
    </div>
    <div class="service" style="left:464px;top:212px">
      <svg class="service-icon" viewBox="0 0 56 50" fill="none" stroke="#c98a2c" stroke-width="2"><circle cx="28" cy="25" r="21"/><circle cx="28" cy="25" r="9"/><circle cx="28" cy="25" r="3"/><path d="M34 6a21 21 0 0 1 14 12l-8 3a12 12 0 0 0-8-7z"/></svg>
      <div><div class="service-title">BRAKE FLUID FLUSH</div><div class="service-desc">Maintain an excellent functioning brake system.<br>Recommended every 2 year or 20,000 miles.</div></div>
    </div>
  </section>

  <div class="product-photo" role="img" aria-label="Photo of an oil bottle, oil filter, red funnel and wrenches"></div>

  <section class="contact">
    <div class="contact-label">CALL NOW AT</div>
    <div class="contact-phone">(833) 555-0148</div>
    <div class="contact-label">EMAIL US AT</div>
    <div class="contact-email">Sales@BrindleFleetCare.com</div>
    <div class="contact-web">WWW.BRINDLEFLEETCARE.COM</div>
  </section>
</main>
</body>
</html>
```